SilverLedgerOak - Double Sided Business Card

We are looking for design options or our business cards. We are a Business Solutions and HR solutions Provider - the theme is business, for this card.

Our brand colours are represented within our logo.

Details needed to be put on the front of the business card are:

Employees name: [Sample Name]
Role: [Sample Role]

Address: Suite 4 - Level 3/48 Halloran Avenue Parramatta NSW 2150
M: 0000 000 000
P: 1300 847 213
F: 1300 847 286
E: sample@silverledgeroak.com.au
www.silverledgeroak.com.au
Updates

Reason: Hello, could we please increase our deadline by 5 days. Thanking you, Tess

Target Market(s)

Business Owners, also Candidates looking for Employment

Industry/Entity Type

Business

Contact Information for Business Card

Role: [Sample Role]

M: 0000 000 000
P: 1300 847 213
F: 1300 847 286

Font styles to use
Sans Serif

Colors
3276b5
3176b5
0455a3
85abd2
cfdeed
ffffff
000000
1b1b1b
757575

Requirements
Must have
• Details needed to be put on the front of the business card are:
• Employees name: [Sample Name]
• Role: [Sample Role]
• Address: Suite 4 - Level 3/48 Halloran Avenue Parramatta NSW 2150
• M: 0000 000 000
• P: 1300 847 213
• F: 1300 847 286
• E: sample@silverledgeroak.com.au
• www.silverledgeroak.com.au
Nice to have
• Simplicity, clean and professional.

```html
<!DOCTYPE html>
<html lang="en">
<head>
<meta charset="utf-8">
<title>SilverLedgerOak – Business Card</title>
<link rel="stylesheet" href="https://fonts.googleapis.com/css2?family=Roboto:wght@400;500;700;900&display=swap">
<style>
  :root {
    --brand-blue: #3276b5;
    --brand-deep: #0455a3;
    --brand-navy: #1c3a5e;
    --brand-light: #85abd2;
    --brand-pale: #cfdeed;
    --white: #ffffff;
    --black: #000000;
    --ink: #1b1b1b;
    --grey: #757575;
    --stage: #e6e8eb;
  }
  * { box-sizing: border-box; margin: 0; padding: 0; }
  html, body {
    width: 1200px; height: 900px; overflow: hidden;
    background: var(--stage);
    font-family: "Roboto", Arial, sans-serif;
  }
  .card {
    position: absolute;
    width: 640px; height: 360px;
    border-radius: 4px;
    overflow: hidden;
    box-shadow: 0 10px 30px rgba(0,0,0,.18);
  }
  /* ---------- back ---------- */
  .card-back {
    left: 440px; top: 60px;
    background: linear-gradient(135deg, #262626 0%, #0d0d0d 45%, var(--black) 100%);
  }
  .card-back .brand {
    position: absolute; right: 40px; top: 200px;
    text-align: left; width: 300px;
  }
  .brand-row { display: flex; align-items: center; gap: 10px; }
  .brand-square {
    width: 22px; height: 22px; background: var(--brand-blue); flex: none;
  }
  .brand-name {
    font-weight: 900; font-size: 29px; letter-spacing: -.3px; line-height: 1;
  }
  .card-back .brand-name { color: var(--white); }
  .brand-rule { height: 1px; margin: 10px 0 6px; }
  .card-back .brand-rule { background: var(--grey); }
  .tagline { font-size: 10.5px; font-weight: 700; letter-spacing: -.1px; }
  .card-back .tagline { color: var(--white); }

  /* ---------- front ---------- */
  .card-front {
    left: 120px; top: 470px;
    background: var(--white);
  }
  .person { position: absolute; left: 40px; top: 34px; padding-left: 14px; }
  .person::before {
    content: ""; position: absolute; left: 0; top: 2px;
    width: 5px; height: 30px; background: var(--brand-deep);
  }
  .person-name { color: var(--brand-deep); font-weight: 700; font-size: 19px; }
  .person-role { color: var(--grey); font-size: 13px; margin-top: 2px; }

  .contacts { position: absolute; left: 40px; top: 178px; list-style: none; }
  .contacts li {
    display: flex; align-items: center; gap: 7px;
    color: var(--grey); font-size: 15px; line-height: 23px;
  }
  .contact-icon { width: 15px; height: 15px; flex: none; }

  .card-front .brand { position: absolute; right: 40px; top: 120px; width: 290px; }
  .card-front .brand-name { color: var(--brand-navy); }
  .card-front .brand-rule { background: var(--brand-light); }
  .card-front .tagline { color: var(--ink); }

  .address {
    position: absolute; right: 40px; top: 228px;
    text-align: right; font-size: 15px; line-height: 21px; color: var(--grey);
    font-style: normal;
  }
  .address-label { color: var(--brand-deep); font-weight: 500; }
  .footer-bands { position: absolute; left: 0; bottom: 0; width: 640px; height: 80px; }
  .website {
    position: absolute; right: 40px; bottom: 9px;
    color: var(--white); font-size: 15px; font-weight: 500;
    white-space: nowrap;
  }
</style>
</head>
<body>

<section class="card card-back" aria-label="Card back">
  <div class="brand">
    <div class="brand-row">
      <span class="brand-square"></span>
      <span class="brand-name">SilverLedgerOak</span>
    </div>
    <div class="brand-rule"></div>
    <p class="tagline">Helping small to medium business realise their potential</p>
  </div>
</section>

<section class="card card-front" aria-label="Card front">
  <div class="person">
    <p class="person-name">Liam Forsyth</p>
    <p class="person-role">Managing Director</p>
  </div>

  <ul class="contacts">
    <li>
      <svg class="contact-icon" viewBox="0 0 16 16" aria-hidden="true"><circle cx="8" cy="8" r="7.2" fill="none" stroke="#0455a3" stroke-width="1.2"/><rect x="5.6" y="3.8" width="4.8" height="8.4" rx="0.8" fill="none" stroke="#0455a3" stroke-width="1.1"/></svg>
      0000 000 000
    </li>
    <li>
      <svg class="contact-icon" viewBox="0 0 16 16" aria-hidden="true"><circle cx="8" cy="8" r="7.2" fill="none" stroke="#0455a3" stroke-width="1.2"/><path d="M5.2 4.2c-.8.7-.9 1.9 0 3.4 1 1.7 2.4 3 4 3.9 1 .5 1.9.4 2.5-.4l-1.5-1.4-1 .6c-.9-.5-1.7-1.3-2.2-2.2l.6-1z" fill="#0455a3"/></svg>
      1300 847 213
    </li>
    <li>
      <svg class="contact-icon" viewBox="0 0 16 16" aria-hidden="true"><circle cx="8" cy="8" r="7.2" fill="none" stroke="#0455a3" stroke-width="1.2"/><rect x="4" y="6.5" width="8" height="4.5" rx=".6" fill="#0455a3"/><rect x="5.5" y="4" width="5" height="2.5" fill="none" stroke="#0455a3" stroke-width="1"/></svg>
      1300 847 286
    </li>
    <li>
      <svg class="contact-icon" viewBox="0 0 16 16" aria-hidden="true"><circle cx="8" cy="8" r="7.2" fill="none" stroke="#0455a3" stroke-width="1.2"/><rect x="4" y="5" width="8" height="6" fill="none" stroke="#0455a3" stroke-width="1.1"/><path d="M4 5l4 3.3L12 5" fill="none" stroke="#0455a3" stroke-width="1.1"/></svg>
      sample@silverledgeroak.com.au
    </li>
  </ul>

  <div class="brand">
    <div class="brand-row">
      <span class="brand-square"></span>
      <span class="brand-name">SilverLedgerOak</span>
    </div>
    <div class="brand-rule"></div>
    <p class="tagline">Helping small to medium business realise their potential</p>
  </div>

  <address class="address">
    <span class="address-label">Address:</span><br>
    Suite 4 - Level 3/48<br>
    Halloran Avenue<br>
    Parramatta NSW 2150
  </address>

  <svg class="footer-bands" viewBox="0 0 640 80" preserveAspectRatio="none" aria-hidden="true">
    <path d="M0 20 H350 L372 38 H640 V41 H371 L349 23 H0 Z" fill="#85abd2"/>
    <path d="M0 27 H344 L368 44 H380 Q366 45 360 48 L342 31 H0 Z" fill="#3276b5"/>
    <path d="M380 44 H640 V80 H350 Q362 48 380 44 Z" fill="#1c3a5e"/>
  </svg>
  <p class="website">www.silverledgeroak.com.au</p>
</section>

</body>
</html>
```